Catering Menu

We are looking at revamping our catering menu to appeal to the corporate and home catering Market.
Attached is our current menu. These items are current, and are required on the new design.
Pictures to be added of platters of what we offer
we are a upmarket venue in Melbourne Australia
we are looking to offer an off site catering option for our clients.
we are aiming to appeal to home celebrations, office and corporate functions.
The menu must pop, and catch the eye of the customer.
this will be done in a mail drop also.
6 sided DL flyer.

Target Market(s)

General Catering for businesses & people at home

Industry/Entity Type

Restaurant

Requirements
Must have
• Pictures of catering food, clear lay out of menu and pricing

```html
<!DOCTYPE html>
<html lang="en">
<head>
<meta charset="utf-8">
<title>Flintwood Catering Menu</title>
<link href="https://fonts.googleapis.com/css2?family=Oswald:wght@400;600&family=Open+Sans:wght@400;600&display=swap" rel="stylesheet">
<style>
:root{
  --page:#ffffff;
  --charcoal:#262626;
  --graphite:#3b3b3b;
  --steel:#4a4a4a;
  --orange:#ec8a1e;
  --amber:#f5a623;
  --text:#e4e4e4;
  --muted:#a9a9a9;
  --photo-warm-a:#7a4a26;
  --photo-warm-b:#c98a4a;
  --photo-room-a:#2d241d;
  --photo-room-b:#6b5846;
}
*{box-sizing:border-box;margin:0;padding:0}
html,body{width:829px;height:1200px;overflow:hidden;background:var(--page)}
body{position:relative;font-family:"Open Sans",Arial,sans-serif;color:var(--text)}
.sheet{position:absolute;display:flex;box-shadow:0 4px 12px rgba(0,0,0,.45);overflow:hidden}
.sheet--outside{left:50px;top:22px;width:750px;height:563px}
.sheet--inside{left:28px;top:620px;width:772px;height:567px}
.panel{position:relative;flex:1;height:100%;background:linear-gradient(180deg,var(--graphite),var(--charcoal));overflow:hidden;border-right:1px solid #1c1c1c}
.panel:last-child{border-right:none}
.photo{position:absolute;display:block}
.photo--room{background:linear-gradient(160deg,var(--photo-room-a),var(--photo-room-b) 60%,var(--photo-room-a))}
.photo--food{background:radial-gradient(circle at 40% 45%,#d8c08a,var(--photo-warm-b) 40%,var(--photo-warm-a))}
.photo--platter{background:linear-gradient(150deg,#d6d0c4,#9a8e7c 55%,#5a4f44)}
.swoosh{position:absolute;left:0;width:100%}
.menu{position:absolute;left:14px;right:14px}
.section-title{font-family:"Oswald",Arial,sans-serif;font-weight:600;font-size:7px;letter-spacing:.3px;color:var(--orange);text-transform:uppercase;margin:7px 0 2px}
.item{display:flex;justify-content:space-between;font-size:4.6px;line-height:6.2px;color:var(--text)}
.item .price{color:var(--amber);padding-left:6px}
.desc{font-size:4.2px;line-height:5.6px;color:var(--muted);margin-bottom:2px}
.order{position:absolute;left:0;right:0;top:252px;text-align:center}
.order h3{font-family:"Oswald",Arial,sans-serif;font-weight:400;font-size:11px;color:#fff;letter-spacing:.5px;margin-bottom:6px}
.order p{font-size:5.4px;line-height:8px;color:var(--text)}
.cover{background:linear-gradient(180deg,#5a5a5a,#3a3a3a)}
.brand{position:absolute;left:0;right:0;top:282px;display:flex;justify-content:center;align-items:center;gap:6px}
.brand__mark{width:10px;height:10px;background:var(--orange)}
.brand__name{font-family:"Oswald",Arial,sans-serif;font-weight:600;font-size:20px;color:#f1f1f1;letter-spacing:1px}
.cover__title{position:absolute;left:0;right:0;top:316px;text-align:center;font-family:"Oswald",Arial,sans-serif;font-weight:600;font-size:22px;color:var(--orange)}
.cover__tagline{position:absolute;left:0;right:0;top:348px;text-align:center;font-size:8px;line-height:11px;color:#eee}
.heading-band{position:absolute;left:10px;right:10px;top:10px;background:var(--orange);padding:3px 6px;font-family:"Oswald",Arial,sans-serif;font-weight:600;font-size:7.5px;color:#fff;text-transform:uppercase;border-radius:2px}
</style>
</head>
<body>

<!-- Outside of the trifold -->
<section class="sheet sheet--outside">
  <div class="panel">
    <div class="photo photo--room" role="img" aria-label="Restaurant dining room interior" style="left:0;top:0;width:100%;height:72px"></div>
    <svg class="swoosh" style="top:52px" width="250" height="34" viewBox="0 0 250 34"><path d="M0 22 Q120 0 250 6 L250 34 L0 34Z" fill="var(--orange)"/><path d="M0 28 Q120 8 250 12 L250 34 L0 34Z" fill="var(--graphite)"/></svg>
    <div class="menu" style="top:82px">
      <div class="section-title">Breakfast</div>
      <div class="item"><span>Mini pastry platter</span><span class="price">$45.00</span></div>
      <div class="desc">Croissants, danish and muffins, baked fresh each morning</div>
      <div class="item"><span>Seasonal fruit platter</span><span class="price">$50.00</span></div>
      <div class="desc">Sliced melon, berries and tropical fruit with yoghurt</div>
      <div class="item"><span>Bircher muesli cups</span><span class="price">$4.50</span></div>
      <div class="item"><span>Bacon and egg rolls</span><span class="price">$6.50</span></div>
      <div class="section-title">Morning &amp; Afternoon Tea</div>
      <div class="item"><span>Scones with jam and cream</span><span class="price">$42.00</span></div>
      <div class="item"><span>Assorted slice platter</span><span class="price">$48.00</span></div>
      <div class="desc">Caramel, lemon and chocolate slices, cut into bites</div>
      <div class="item"><span>Mini quiche selection</span><span class="price">$40.00</span></div>
      <div class="item"><span>Cake of the day</span><span class="price">$38.00</span></div>
      <div class="section-title">Finger Food</div>
      <div class="item"><span>Arancini balls, aioli</span><span class="price">$36.00</span></div>
      <div class="item"><span>Chicken skewers, satay</span><span class="price">$44.00</span></div>
      <div class="item"><span>Vegetable spring rolls</span><span class="price">$32.00</span></div>
      <div class="item"><span>Beef sliders</span><span class="price">$54.00</span></div>
      <div class="section-title">Antipasto &amp; Cheese</div>
      <div class="item"><span>Antipasto board</span><span class="price">$65.00</span></div>
      <div class="desc">Cured meats, olives, grilled vegetables and breads</div>
      <div class="item"><span>Local cheese board</span><span class="price">$70.00</span></div>
      <div class="desc">Three cheeses, quince paste, lavosh and fresh fruit</div>
      <div class="section-title">Drinks</div>
      <div class="item"><span>Juice jugs, orange or apple</span><span class="price">$12.00</span></div>
      <div class="item"><span>Sparkling water</span><span class="price">$4.00</span></div>
    </div>
  </div>

  <div class="panel">
    <svg class="swoosh" style="top:0" width="250" height="50" viewBox="0 0 250 50"><path d="M0 0 H250 V18 Q120 44 0 30Z" fill="var(--steel)"/></svg>
    <svg style="position:absolute;left:65px;top:88px" width="120" height="120" viewBox="0 0 120 120"><circle cx="60" cy="60" r="58" fill="var(--orange)"/></svg>
    <div class="photo photo--food" role="img" aria-label="Asian noodle salad in a bowl" style="left:70px;top:93px;width:110px;height:110px;border-radius:50%"></div>
    <div class="order">
      <h3>TO ORDER PLEASE</h3>
      <p>Call (03) 9000 1234<br>orders@flintwoodkitchen.com.au<br>www.flintwoodkitchen.com.au<br>Flintwood Events Centre<br>Ph (03) 9000 1235<br>88 Laneway Street, Melbourne</p>
    </div>
    <svg class="swoosh" style="bottom:0" width="250" height="60" viewBox="0 0 250 60"><path d="M0 30 Q130 0 250 24 V60 H0Z" fill="var(--orange)"/><path d="M0 38 Q130 10 250 32 V60 H0Z" fill="var(--charcoal)"/></svg>
  </div>

  <div class="panel cover">
    <div class="photo photo--food" role="img" aria-label="Grilled chicken with salad and dipping sauce" style="left:0;top:0;width:100%;height:230px"></div>
    <svg class="swoosh" style="top:190px" width="250" height="70" viewBox="0 0 250 70"><path d="M0 40 Q120 -10 250 20 V70 H0Z" fill="var(--orange)"/><path d="M0 50 Q120 2 250 30 V70 H0Z" fill="#555"/></svg>
    <div class="brand"><span class="brand__mark"></span><span class="brand__name">FLINTWOOD</span></div>
    <div class="cover__title">CATERING MENU</div>
    <div class="cover__tagline">Your guide to our platter<br>options available</div>
    <svg class="swoosh" style="bottom:0" width="250" height="50" viewBox="0 0 250 50"><path d="M0 20 Q120 50 250 10 V50 H0Z" fill="var(--orange)"/><path d="M0 28 Q120 56 250 18 V50 H0Z" fill="var(--charcoal)"/></svg>
  </div>
</section>

<!-- Inside of the trifold -->
<section class="sheet sheet--inside">
  <div class="panel">
    <div class="heading-band">Hot Lunch Platters</div>
    <div class="menu" style="top:26px">
      <div class="item"><span>Roast beef platter</span><span class="price">$14.50pp</span></div>
      <div class="desc">Slow roasted beef with gravy, roast potatoes and seasonal greens</div>
      <div class="item"><span>Chicken cacciatore</span><span class="price">$13.50pp</span></div>
      <div class="desc">Braised chicken in tomato and olive sauce with steamed rice</div>
      <div class="item"><span>Beef lasagne tray</span><span class="price">$12.00pp</span></div>
      <div class="desc">Layered pasta, rich ragu and bechamel, served with garden salad</div>
      <div class="item"><span>Thai green curry</span><span class="price">$13.00pp</span></div>
      <div class="desc">Chicken or vegetable curry with jasmine rice and fresh herbs</div>
      <div class="item"><span>Lamb souvlaki</span><span class="price">$15.00pp</span></div>
      <div class="desc">Marinated lamb, tzatziki, warm pita and tomato salad</div>
      <div class="item"><span>Pumpkin risotto</span><span class="price">$11.50pp</span></div>
      <div class="desc">Roast pumpkin, spinach, parmesan and toasted pepitas</div>
      <div class="item"><span>Gourmet pie platter</span><span class="price">$12.50pp</span></div>
      <div class="desc">Beef, chicken leek and vegetable pies with relish</div>
      <div class="item"><span>Crumbed fish platter</span><span class="price">$14.00pp</span></div>
      <div class="desc">Local fish, chips, lemon wedges and tartare sauce</div>
      <div class="item"><span>Penne boscaiola</span><span class="price">$11.00pp</span></div>
      <div class="desc">Bacon, mushroom and cream sauce with shaved parmesan</div>
      <div class="item"><span>Pork belly bites</span><span class="price">$15.50pp</span></div>
      <div class="desc">Crisp pork belly with apple slaw and sticky glaze</div>
      <div class="section-title" style="margin-top:12px">Cold Lunch Platters</div>
      <div class="item"><span>Cold meat platter</span><span class="price">$13.00pp</span></div>
      <div class="desc">Ham, turkey and roast beef with pickles and breads</div>
      <div class="item"><span>Poached salmon</span><span class="price">$16.00pp</span></div>
      <div class="desc">Whole side of salmon, dill cream and cucumber</div>
      <div class="item"><span>Chicken platter</span><span class="price">$12.50pp</span></div>
      <div class="desc">Roast chicken pieces with salads and dressings</div>
      <div class="item"><span>Prawn platter</span><span class="price">$18.00pp</span></div>
      <div class="desc">Cooked king prawns, cocktail sauce and lemon</div>
    </div>
  </div>

  <div class="panel">
    <div class="heading-band">Sandwiches/Wraps/Focaccia Platters</div>
    <div class="menu" style="top:26px">
      <div class="item"><span>Classic sandwich platter</span><span class="price">$48.00</span></div>
      <div class="desc">Ham, egg, chicken and salad fillings on white and grain bread</div>
      <div class="item"><span>Gourmet wrap platter</span><span class="price">$55.00</span></div>
      <div class="desc">Chicken caesar, falafel hummus and beef with relish</div>
      <div class="item"><span>Focaccia platter</span><span class="price">$60.00</span></div>
      <div class="desc">Toasted focaccia with prosciutto, brie and roast vegetables</div>
      <div class="item"><span>Mini roll platter</span><span class="price">$52.00</span></div>
      <div class="desc">Soft rolls with assorted cold cuts and fresh salad</div>
      <div class="item"><span>Vegetarian platter</span><span class="price">$46.00</span></div>
      <div class="desc">Egg, cheese, avocado and roasted capsicum fillings</div>
      <div class="item"><span>Ribbon sandwiches</span><span class="price">$44.00</span></div>
    </div>
    <div class="photo photo--platter" role="img" aria-label="Sandwich platter on a buffet table" style="left:0;top:330px;width:100%;height:237px"></div>
    <svg class="swoosh" style="top:318px" width="257" height="40" viewBox="0 0 257 40"><path d="M0 8 Q130 34 257 6 V14 Q130 40 0 16Z" fill="var(--orange)"/><path d="M0 0 H257 V6 Q130 34 0 8Z" fill="var(--charcoal)"/></svg>
    <svg style="position:absolute;left:150px;top:300px" width="74" height="74" viewBox="0 0 74 74"><circle cx="37" cy="37" r="36" fill="var(--orange)"/></svg>
    <div class="photo photo--food" role="img" aria-label="Wrap platter close up" style="left:153px;top:303px;width:68px;height:68px;border-radius:50%"></div>
  </div>

  <div class="panel">
    <div class="heading-band">Cold Dishes</div>
    <div class="menu" style="top:26px">
      <div class="item"><span>Sushi platter</span><span class="price">$58.00</span></div>
      <div class="desc">Assorted rolls with soy, wasabi and pickled ginger</div>
      <div class="item"><span>Rice paper rolls</span><span class="price">$42.00</span></div>
      <div class="item"><span>Smoked salmon blinis</span><span class="price">$48.00</span></div>
      <div class="item"><span>Bruschetta platter</span><span class="price">$38.00</span></div>
      <div class="desc">Tomato, basil and garlic on toasted baguette</div>
      <div class="section-title" style="margin-top:10px">Salads</div>
      <div class="item"><span>Caesar salad</span><span class="price">$40.00</span></div>
      <div class="desc">Cos lettuce, bacon, croutons, parmesan and egg</div>
      <div class="item"><span>Greek salad</span><span class="price">$38.00</span></div>
      <div class="item"><span>Thai beef salad</span><span class="price">$46.00</span></div>
      <div class="desc">Seared beef, noodles, herbs and lime dressing</div>
      <div class="item"><span>Roast vegetable salad</span><span class="price">$36.00</span></div>
      <div class="item"><span>Pasta salad</span><span class="price">$34.00</span></div>
      <div class="item"><span>Garden salad</span><span class="price">$30.00</span></div>
    </div>
    <svg class="swoosh" style="top:372px" width="257" height="40" viewBox="0 0 257 40"><path d="M0 24 Q130 0 257 20 V40 H0Z" fill="var(--orange)"/></svg>
    <div class="photo photo--platter" role="img" aria-label="Catered buffet with platters served at a function" style="left:0;top:384px;width:100%;height:183px;clip-path:path('M0 16 Q130 -6 257 12 V183 H0Z')"></div>
  </div>
</section>

</body>
</html>
```